Epoxy coatings company needs a logo/business card design.

My company name is "Lustrous Resin Works", and I am looking for a company logo and business card design.
My initial thought was to use "Æ"in 'Lu'strous, and would also like to see ideas on how to play around with the fact that the first 3 letters (Lrw) are also the acronym of the company name.
I specialize in garage floor and interior epoxy coatings, paint flake broadcasts, quartz broadcasts, and solid color epoxy floors, concrete repairs.
I like images I've seen of a silhouetted person running a floor grinder. It keeps the design of the card simple. I'm not necessarily opposed to using images of the floors on the card, but I'd prefer to keep the front simple (Company name, my name, phone number, email) and maybe put pictures on the back. I've included a few of my personal pictures of floors I've done (including a before, after, and when the garage was being used after)
My colors are darker green (Fern/Forest/Hunter, etc), and Bronze.

Contact Information for Business Card

Name: Dana Kellworth Email: lustrousresinworks@mailbrook.net Phone: (555)318-9042 Instagram: lustrous_resin_works

Colors

Designer to choose colors to be used in the design.

Requirements
Nice to have
• I've included a business card designed for someone else, that contains the silhouette that I'm looking for. The floor grinder that I use is large like the one pictured (Torvex G40R).

```html
<!DOCTYPE html>
<html lang="en">
<head>
<meta charset="utf-8">
<title>Lustrous Resin Works – Business Card</title>
<link href="https://fonts.googleapis.com/css2?family=Lato:wght@400;700&family=Montserrat:wght@600&display=swap" rel="stylesheet">
<style>
  :root {
    --forest: #1e8a3e;
    --bronze: #4a261f;
    --bronze-light: #57302a;
    --ink: #4a261f;
    --paper: #ffffff;
    --backdrop: #ffffff;
  }
  html, body {
    margin: 0;
    padding: 0;
    width: 1200px;
    height: 1200px;
    overflow: hidden;
    background: var(--backdrop);
  }
  .canvas {
    position: relative;
    width: 1200px;
    height: 1200px;
  }
  .card {
    position: absolute;
    width: 832px;
    height: 478px;
    box-sizing: border-box;
    overflow: hidden;
  }
  .card--front {
    left: 189px;
    top: 91px;
    background: var(--paper);
    border: 1px solid #e6e6e6;
  }
  .card--back {
    left: 187px;
    top: 639px;
    background: var(--bronze);
  }
  .card__texture {
    position: absolute;
    inset: 0;
    background:
      radial-gradient(ellipse at 50% 45%, var(--bronze-light) 0%, var(--bronze) 70%);
  }
  .brand {
    position: absolute;
    display: flex;
    flex-direction: column;
    align-items: center;
    transform: translateX(-50%);
  }
  .card--front .brand { left: 632px; top: 40px; }
  .card--back .brand { left: 416px; top: 136px; }
  .brand__ring {
    width: 118px;
    height: 118px;
    border-radius: 50%;
    box-sizing: border-box;
    border: 7px solid var(--bronze);
  }
  .card--back .brand__ring { width: 128px; height: 128px; border-color: var(--paper); }
  .brand__name {
    margin-top: 28px;
    font-family: "Montserrat", sans-serif;
    font-weight: 600;
    font-size: 27px;
    letter-spacing: 0.5px;
    color: var(--forest);
    white-space: nowrap;
  }
  .card--back .brand__name {
    margin-top: 32px;
    font-size: 29px;
    color: var(--paper);
  }
  .accent-bar {
    position: absolute;
    left: -1px;
    top: 314px;
    width: 17px;
    height: 128px;
    background: var(--bronze);
  }
  .holder {
    position: absolute;
    left: 42px;
    top: 308px;
  }
  .holder__name {
    margin: 0 0 14px;
    font-family: "Lato", sans-serif;
    font-weight: 700;
    font-size: 31px;
    letter-spacing: -0.3px;
    color: var(--forest);
  }
  .contact {
    list-style: none;
    margin: 0;
    padding: 0;
    font-family: "Lato", sans-serif;
    font-size: 20px;
    color: var(--ink);
  }
  .contact__item {
    display: flex;
    align-items: center;
    height: 28.5px;
  }
  .contact__icon {
    width: 19px;
    height: 19px;
    margin-right: 7px;
    flex: none;
  }
  .contact__dot {
    width: 15px;
    height: 15px;
    margin: 0 8px 0 2px;
    border-radius: 50%;
    border: 2px solid var(--forest);
    box-sizing: border-box;
    flex: none;
  }
</style>
</head>
<body>
<main class="canvas">
  <section class="card card--front" aria-label="Business card front">
    <div class="brand">
      <div class="brand__ring"></div>
      <div class="brand__name">LUSTROUS RESIN WORKS</div>
    </div>
    <div class="accent-bar"></div>
    <div class="holder">
      <h1 class="holder__name">DANA KELLWORTH</h1>
      <ul class="contact">
        <li class="contact__item">
          <svg class="contact__icon" viewBox="0 0 24 24" aria-hidden="true">
            <path fill="#1e8a3e" d="M6.6 10.8c1.4 2.8 3.8 5.1 6.6 6.6l2.2-2.2c.3-.3.7-.4 1-.2 1.1.4 2.300.6 3.6.6.6 0 1 .4 1 1V20c0 .6-.4 1-1 1C10.6 21 3 13.4 3 4c0-.6.4-1 1-1h3.5c.6 0 1 .4 1 1 0 1.3.2 2.5.6 3.6.1.3 0 .7-.2 1z"/>
            <path fill="none" stroke="#1e8a3e" stroke-width="1.8" d="M14 3.5a7 7 0 0 1 6.5 6.5M14 7a3.5 3.5 0 0 1 3 3"/>
          </svg>
          (555)318-9042
        </li>
        <li class="contact__item">
          <svg class="contact__icon" viewBox="0 0 24 24" aria-hidden="true">
            <rect x="2" y="5" width="20" height="14" fill="#1e8a3e"/>
            <path d="M2 5l10 8 10-8M2 19l8-7M22 19l-8-7" fill="none" stroke="#fff" stroke-width="1.6"/>
          </svg>
          lustrousresinworks@mailbrook.net
        </li>
        <li class="contact__item">
          <span class="contact__dot"></span>
          lustrous_resin_works
        </li>
      </ul>
    </div>
  </section>

  <section class="card card--back" aria-label="Business card back">
    <div class="card__texture" role="img" aria-label="Tone-on-tone repeating monogram pattern across the dark bronze card back"></div>
    <div class="brand">
      <div class="brand__ring"></div>
      <div class="brand__name">LUSTROUS RESIN WORKS</div>
    </div>
  </section>
</main>
</body>
</html>
```